Tovenly Website Redesign

We have a web site called tovenly.com that is all about education/information about legal marijuana. We're looking to significantly improve the modern-ness and look/feel of the web site - and to make it look like many of the best web sites out there today.

The task will be to come up with a better design for:
- The home page: http://tovenly.com/
- The logo (see the logo at the top of each page)
- The header and footer (for all the pages)
- The vaporizer page: http://tovenly.com/collections/vaporizer
- The store map page: http://tovenly.com/pages/shop-marijuana-in-colorado-state

The output of the project will be:
- screenshots of the designs and any images needed
- PSD file

Key requirements:
- Style needs to look fresh/modern
- Especially on the vaporizers page, the key things we want to drive is conversion - getting more people to interact with the page and actually click on the links to purchase vaporizers

Reason: Raised the budget and want to give designers a few more days to provide entries.

Note I clarified that I don't need code (HTML or CSS) for the project. I just need the designs, including images and the PSD file. Thanks.

Reason: We're getting closet to selecting a design, just need a few more days to iterate on a few we're working on.

Industry/Entity Type

Education

Font styles to use
Sans Serif

Requirements
Must have
• Must look like a modern/clean/fresh looking website design.

```html
<!DOCTYPE html>
<html lang="en">
<head>
<meta charset="utf-8">
<title>Tovenly — Shop Marijuana in style</title>
<link href="https://fonts.googleapis.com/css2?family=Open+Sans:wght@300;400;600;700;800&display=swap" rel="stylesheet">
<style>
:root{
  --dark:#1d1d1d;
  --darker:#111111;
  --orange:#f7941d;
  --orange-deep:#ef8a10;
  --green:#5fb336;
  --lime:#a5c61c;
  --yellow:#f4c300;
  --bright-green:#29c24e;
  --logo-green:#4fc23a;
  --band:#ecece6;
  --text:#333333;
  --muted:#777777;
  --line:#dddddd;
  --white:#ffffff;
}
*{box-sizing:border-box;margin:0;padding:0}
html,body{width:1200px;height:2752px;overflow:hidden}
body{font-family:"Open Sans",Arial,sans-serif;color:var(--text);background:var(--white)}
.wrap{width:1008px;margin:0 auto;position:relative}

/* header */
.topbar{height:99px;background:var(--dark)}
.topbar .wrap{height:99px;display:flex;align-items:center}
.logo{font-size:62px;font-weight:800;color:var(--logo-green);letter-spacing:-1px;line-height:1}
.tagline{color:var(--white);font-size:17px;margin:24px 0 0 18px}
.account{margin-left:auto;text-align:right;color:var(--white);font-size:13px}
.cart{color:var(--orange);font-size:13px;display:flex;align-items:center;justify-content:flex-end;gap:8px;margin-bottom:14px}
.account-links span{margin-left:14px}
.mainnav{height:56px;background:var(--orange);display:flex;align-items:center;justify-content:space-around;position:relative;z-index:2}
.mainnav a{color:var(--white);text-decoration:none;font-size:18px;padding:0 22px;border-right:1px solid rgba(255,255,255,.35);line-height:56px}
.mainnav a:last-child{border-right:0}
.hero{height:436px;margin-top:-2px;background:radial-gradient(ellipse at 30% 50%,#8b8f5a 0%,#6b6a3e 40%,#b7b08a 75%,#e8e3d2 100%)}

/* feature tiles */
.features{height:278px;background:var(--band);padding-top:27px}
.features .wrap{display:flex;justify-content:space-between}
.tile{width:232px;height:220px;color:var(--white);text-align:center;padding-top:38px}
.tile svg{display:block;margin:0 auto 14px}
.tile h3{font-size:21px;font-weight:800;letter-spacing:.5px}
.tile p{font-size:12px;margin-top:4px;text-transform:uppercase}
.tile.gift{background:var(--green)}
.tile.order{background:var(--lime)}
.tile.ship{background:var(--yellow)}
.tile.save{background:var(--orange)}

/* products */
.collections{height:905px;background:var(--white);padding-top:28px}
.section-title{text-align:center;font-size:36px;font-weight:400;color:#222;line-height:1.3}
.grid{display:grid;grid-template-columns:repeat(4,230px);justify-content:space-between;row-gap:34px;margin-top:22px}
.card{border:1px solid var(--line);height:366px;padding:10px 12px;display:flex;flex-direction:column;overflow:hidden}
.card .photo{height:158px;flex:none;background:linear-gradient(180deg,#f4f4f4,#d9d9d9)}
.card h4{font-size:14px;font-weight:600;line-height:20px;margin-top:14px;white-space:nowrap}
.card .type{font-size:12px;line-height:18px;color:var(--muted);margin-top:10px}
.card .desc{font-size:12px;color:var(--muted);line-height:17px;margin-top:4px}
.price{color:var(--orange-deep);font-weight:700;font-size:19px;line-height:26px;margin-top:8px}
.actions{display:flex;gap:8px;margin-top:auto}
.btn{font-size:11px;color:var(--white);height:30px;line-height:30px;padding:0 12px;font-weight:600;text-transform:uppercase}
.btn.read{background:var(--green)}
.btn.add{background:var(--orange)}

/* blog */
.news{height:452px;background:var(--band);padding-top:47px}
.news .wrap{display:grid;grid-template-columns:490px 496px;justify-content:space-between;row-gap:36px}
.post{height:158px;background:var(--white);display:flex;overflow:hidden}
.post .photo{width:194px;flex:none}
.post .body{padding:10px 14px}
.post h5{font-size:14.5px;font-weight:700;line-height:19px}
.post p{font-size:12px;color:var(--muted);line-height:16px;margin-top:6px}
.post .more{color:var(--orange-deep);font-size:11.5px;font-weight:700;margin-top:6px;display:block}
.ph-a{background:linear-gradient(135deg,#4d3b30,#a98a72)}
.ph-b{background:linear-gradient(135deg,#7a5e50,#c9b7a6)}
.ph-c{background:linear-gradient(135deg,#6c6a3c,#c4b58a)}
.ph-d{background:linear-gradient(135deg,#3a2218,#7a4a34)}

/* contact */
.contact{height:297px;padding-top:38px}
.contact-form{display:grid;grid-template-columns:320px 322px 320px;column-gap:22px;margin-top:18px}
.field{height:36px;border:1px solid #cfcfcf;font-size:13px;padding:8px 10px;color:#444}
.col{display:flex;flex-direction:column;gap:14px}
.field.message{height:86px}
.send{display:block;width:290px;height:50px;margin:26px auto 0;background:var(--bright-green);color:var(--white);font-size:24px;text-align:center;line-height:50px}

/* footer */
.footer{height:185px;background:var(--darker);padding-top:22px;color:var(--white)}
.footer .wrap{display:flex}
.footer h6{font-size:24px;font-weight:400;color:var(--orange)}
.footer .blog h6{color:var(--white)}
.quick{width:296px}
.quick ul{list-style:none;margin-top:8px}
.quick li{font-size:12px;line-height:16px}
.quick li::before{content:"•";color:var(--orange);margin-right:10px}
.blog{width:516px}
.blog strong{display:block;font-size:12.5px;margin-top:10px}
.blog p{font-size:12px;color:#aaaaaa;line-height:1.35;margin-top:4px;width:470px}
.touch ul{list-style:none;margin-top:6px}
.touch li{font-size:12px;display:flex;align-items:center;gap:10px;height:30px}
.touch li i{width:18px;height:18px;background:var(--orange);display:block}
.copyright{height:41px;background:#1b1b1b;color:var(--white);font-size:12px;text-align:center;line-height:41px}
.copyright b{color:var(--logo-green);font-weight:400}
</style>
</head>
<body>

<header>
  <div class="topbar">
    <div class="wrap">
      <div class="logo">Tovenly</div>
      <div class="tagline">Shop Marijuana in style</div>
      <div class="account">
        <div class="cart">
          <svg width="18" height="16" viewBox="0 0 18 16"><path d="M1 2h3l2 8h9l2-6H5" fill="none" stroke="#f7941d" stroke-width="1.8"/><circle cx="7" cy="13.5" r="1.5" fill="#f7941d"/><circle cx="14" cy="13.5" r="1.5" fill="#f7941d"/></svg>
          My Cart: 0 item(s) - $0.00 ▾
        </div>
        <div class="account-links"><span>WishList(0)</span><span>Checkout</span><span>Login</span><span>Create an Account</span></div>
      </div>
    </div>
  </div>
  <nav class="wrap mainnav">
    <a>Home</a><a>About Us</a><a>Blog</a><a>Marijuana 101</a><a>Legal Marijuana</a><a>Vaporizers</a><a>Contact Us</a>
  </nav>
</header>

<div class="hero" role="img" aria-label="Close-up photograph of dried cannabis buds"></div>

<section class="features">
  <div class="wrap">
    <div class="tile gift">
      <svg width="62" height="62" viewBox="0 0 62 62" fill="none" stroke="#fff" stroke-width="4"><rect x="6" y="22" width="50" height="12"/><rect x="10" y="34" width="42" height="24"/><path d="M31 22v36M31 22c-4-12-16-14-16-6s10 6 16 6c6 0 16 2 16-6s-12-6-16 6"/></svg>
      <h3>SPECIAL GIFT</h3><p>Give the perfect gift</p>
    </div>
    <div class="tile order">
      <svg width="70" height="62" viewBox="0 0 70 62" fill="none" stroke="#fff" stroke-width="4"><rect x="4" y="4" width="62" height="44" rx="4"/><rect x="12" y="12" width="46" height="28" fill="#fff" stroke="none" opacity=".25"/><path d="M30 30v-10l12 10h-6l4 10"/><circle cx="35" cy="55" r="3" fill="#fff"/></svg>
      <h3>ORDER ONLINE</h3><p>Hours : 8am - 11am</p>
    </div>
    <div class="tile ship">
      <svg width="72" height="62" viewBox="0 0 72 62" fill="none" stroke="#fff" stroke-width="4"><rect x="4" y="12" width="38" height="30"/><path d="M42 22h14l10 12v8H42z"/><circle cx="16" cy="48" r="6" fill="#f4c300"/><circle cx="54" cy="48" r="6" fill="#f4c300"/></svg>
      <h3>FREE SHIPPING</h3><p>On orders over $99</p>
    </div>
    <div class="tile save">
      <svg width="68" height="62" viewBox="0 0 68 62" fill="none" stroke="#fff" stroke-width="4"><path d="M2 6h10l8 32h36l8-22H16"/><path d="M24 24h34M26 31h30"/><circle cx="24" cy="50" r="5"/><circle cx="52" cy="50" r="5"/></svg>
      <h3>SHOP &amp; SAVE</h3><p>For all game controls</p>
    </div>
  </div>
</section>

<section class="collections">
  <div class="wrap">
    <h2 class="section-title">Curated Collections</h2>
    <div class="grid">
      <div class="card"><div class="photo" role="img" aria-label="Black portable vaporizer product photo"></div><h4>Crest Vaporizer by Ravello</h4><div class="type">Type: Portable</div><p class="desc">The latest high quality vaporizer by Ravello, the Crest...</p><div class="price">$250.00</div><div class="actions"><span class="btn read">Read More</span><span class="btn add">Add to Cart</span></div></div>
      <div class="card"><div class="photo" role="img" aria-label="Desktop vaporizer unit product photo"></div><h4>Crest Vaporizer by Ravello</h4><div class="type">Type: Portable</div><p class="desc">The latest high quality vaporizer by Ravello, the Crest...</p><div class="price">$250.00</div><div class="actions"><span class="btn read">Read More</span><span class="btn add">Add to Cart</span></div></div>
      <div class="card"><div class="photo" role="img" aria-label="Wooden pipe vaporizer product photo"></div><h4>Crest Vaporizer by Ravello</h4><div class="type">Type: Portable</div><p class="desc">The latest high quality vaporizer by Ravello, the Crest...</p><div class="price">$250.00</div><div class="actions"><span class="btn read">Read More</span><span class="btn add">Add to Cart</span></div></div>
      <div class="card"><div class="photo" role="img" aria-label="Handheld heat wand vaporizer product photo"></div><h4>Crest Vaporizer by Ravello</h4><div class="type">Type: Portable</div><p class="desc">The latest high quality vaporizer by Ravello, the Crest...</p><div class="price">$250.00</div><div class="actions"><span class="btn read">Read More</span><span class="btn add">Add to Cart</span></div></div>
      <div class="card"><div class="photo" role="img" aria-label="Round metal vaporizer product photo"></div><h4>Crest Vaporizer by Ravello</h4><div class="type">Type: Portable</div><p class="desc">The latest high quality vaporizer by Ravello, the Crest...</p><div class="price">$250.00</div><div class="actions"><span class="btn read">Read More</span><span class="btn add">Add to Cart</span></div></div>
      <div class="card"><div class="photo" role="img" aria-label="Pen style vaporizer product photo"></div><h4>Crest Vaporizer by Ravello</h4><div class="type">Type: Portable</div><p class="desc">The latest high quality vaporizer by Ravello, the Crest...</p><div class="price">$250.00</div><div class="actions"><span class="btn read">Read More</span><span class="btn add">Add to Cart</span></div></div>
      <div class="card"><div class="photo" role="img" aria-label="Compact black vaporizer product photo"></div><h4>Crest Vaporizer by Ravello</h4><div class="type">Type: Portable</div><p class="desc">The latest high quality vaporizer by Ravello, the Crest...</p><div class="price">$250.00</div><div class="actions"><span class="btn read">Read More</span><span class="btn add">Add to Cart</span></div></div>
      <div class="card"><div class="photo" role="img" aria-label="Vaporizer with handle product photo"></div><h4>Crest Vaporizer by Ravello</h4><div class="type">Type: Portable</div><p class="desc">The latest high quality vaporizer by Ravello, the Crest...</p><div class="price">$250.00</div><div class="actions"><span class="btn read">Read More</span><span class="btn add">Add to Cart</span></div></div>
    </div>
  </div>
</section>

<section class="news">
  <div class="wrap">
    <article class="post"><div class="photo ph-a" role="img" aria-label="Photo of a hand lighting a joint"></div><div class="body"><h5>Denver Man Admits Smoking Weed Was More Fun When It Was Illegal</h5><p>Dale Morrow, a marijuana enthusiast living in the Denver area, told reporters Wednesday that he enjoyed getting high more when it was illegal.</p><span class="more">READ MORE</span></div></article>
    <article class="post"><div class="photo ph-b" role="img" aria-label="Photo of a man relaxing on a couch"></div><div class="body"><h5>New Colorado Springs Smoker Accepting Potential Obesity</h5><p>Stating that legal marijuana is just "too damn convenient" and makes food taste "too damn good," Glen Parker, a 28-year-old mechanic living in Colorado Springs...</p><span class="more">READ MORE</span></div></article>
    <article class="post"><div class="photo ph-c" role="img" aria-label="Photo of hands holding cannabis"></div><div class="body"><h5>The 6 Best Ways to Store Your Weed</h5><p>There's nothing worse than opening up your stash and finding out that your weed has completely dried out and stale. To help you, here is how to keep it fresh for longer.</p><span class="more">READ MORE</span></div></article>
    <article class="post"><div class="photo ph-d" role="img" aria-label="Photo of chocolate brownies"></div><div class="body"><h5>The Best Ways To Take Marijuana (And Their Effects)</h5><p>There are many ways to get high and a lot of them have different effects. So here's our list of the best ways to get high and the different ways you'll feel it...</p><span class="more">READ MORE</span></div></article>
  </div>
</section>

<section class="contact">
  <div class="wrap">
    <h2 class="section-title">Quick Contact</h2>
    <div class="contact-form">
      <div class="col"><div class="field">Name</div><div class="field">Phone</div></div>
      <div class="col"><div class="field">Email</div><div class="field">Subject</div></div>
      <div class="col"><div class="field message">Massage</div></div>
    </div>
    <span class="send">Send Massage</span>
  </div>
</section>

<footer>
  <div class="footer">
    <div class="wrap">
      <div class="quick"><h6>Quick Links</h6><ul><li>Home</li><li>About us</li><li>Blog</li><li>Faq</li><li>Contact us</li></ul></div>
      <div class="blog"><h6>Latest Blog</h6><strong>The first Marijuana Billboards are up: right thing for me and my family?</strong><p>The first marijuana billboards are coming up in Washington State, and they're pretty cool. The billboards are pretty non-descript - can't tell what they want or what they're selling there's...</p></div>
      <div class="touch"><h6>Get in Touch</h6><ul><li><i></i>Be a fan on Circlebook</li><li><i></i>Rss Feed</li><li><i></i>Follow us on Vidstream</li></ul></div>
    </div>
  </div>
  <div class="copyright">Copyright © 2014 <b>Tovenly</b></div>
</footer>

</body>
</html>
```